Hörbuchcover
Zielgruppe
Spiritueller Hörbuchverlag für ganzheitliche Gesundheit, Glück und Wohlstand.
Aufgabenstellung
Benötigt wird ein schönes quadratisches Cover, 2400x2400 mindestens 72dpi für ein Hörbuchcover.
Auf dem Cover soll eine gelb/orange Rose zu in Form einer Blüte zu sehen sein.
Titel: Innere Wandlung
Untertitel: Emotionen sind der Schlüssel für Gesundheit, Energie & Lebensfreude
Autorenname: Dr. med. Birgit Wolkenstein
Das Feloria Logo soll unten mittig sitzen.
Es folgen weiterer Hörbücher von dieser Autorin und es wäre gut wenn man die folgenden Cover in einem ähnlichen Stil halten könnte. Ein harmonisches und gut zu erkennendes Design mit hohem Wiedererkennungseffekt. Ich freue mich auf kreative Designvorschläge.
Auf feloria.de kann man sehen wo das Logo sitzen soll.
Herzliche Grüße - Jens

```html
<!DOCTYPE html>
<html lang="de">
<head>
<meta charset="utf-8">
<title>Innere Wandlung – Hörbuchcover</title>
<link rel="stylesheet" href="https://fonts.googleapis.com/css2?family=Fira+Sans:ital,wght@0,400;0,600;1,600&display=swap">
<style>
  :root {
    --stage: #1f1b1b;
    --paper: #ffffff;
    --title: #e85a36;
    --ink: #1a1616;
    --rose-light: #f6b48f;
    --rose-mid: #ef8a5e;
    --rose-deep: #e0603f;
    --rose-pale: #fbe3d2;
  }
  * { margin: 0; padding: 0; box-sizing: border-box; }
  html, body {
    width: 1200px;
    height: 2177px;
    overflow: hidden;
    background: var(--stage);
  }
  .stage {
    position: relative;
    width: 1200px;
    height: 2177px;
  }
  .cover {
    position: absolute;
    left: 84px;
    top: 573px;
    width: 1031px;
    height: 1031px;
    background: var(--paper);
    overflow: hidden;
    font-family: "Fira Sans", sans-serif;
  }
  .cover__rose {
    position: absolute;
    left: -20px;
    top: 228px;
    width: 650px;
    height: 820px;
    border-radius: 46% 54% 40% 30% / 38% 42% 30% 20%;
    background:
      radial-gradient(circle at 38% 30%, var(--rose-light) 0%, transparent 45%),
      radial-gradient(circle at 30% 60%, var(--rose-deep) 0%, transparent 55%),
      radial-gradient(circle at 70% 55%, var(--rose-pale) 0%, transparent 50%),
      linear-gradient(160deg, var(--rose-mid), var(--rose-deep));
  }
  .cover__title {
    position: absolute;
    right: 64px;
    top: 30px;
    text-align: right;
    color: var(--title);
    font-weight: 600;
    font-size: 136px;
    line-height: 146px;
    letter-spacing: 1px;
  }
  .cover__subtitle {
    position: absolute;
    right: 64px;
    top: 512px;
    text-align: right;
    color: var(--ink);
    font-style: italic;
    font-weight: 600;
    font-size: 37px;
    line-height: 43px;
  }
  .cover__author {
    position: absolute;
    right: 64px;
    top: 700px;
    text-align: right;
    color: var(--ink);
    font-weight: 400;
    font-size: 38px;
    line-height: 41px;
  }
  .publisher {
    position: absolute;
    left: 515px;
    top: 848px;
    transform: translateX(-50%);
    display: flex;
    flex-direction: column;
    align-items: center;
    gap: 14px;
  }
  .publisher__dot {
    width: 80px;
    height: 80px;
    border-radius: 50%;
    background: var(--ink);
  }
  .publisher__name {
    color: var(--ink);
    font-weight: 400;
    font-size: 56px;
    line-height: 60px;
    letter-spacing: 6px;
    text-transform: uppercase;
  }
</style>
</head>
<body>
  <main class="stage">
    <section class="cover">
      <div class="cover__rose" role="img" aria-label="Aquarellierte orangefarbene Rosenblüte"></div>
      <h1 class="cover__title">Innere<br>Wandlung</h1>
      <p class="cover__subtitle">Emotionen sind<br>der Schlüssel für<br>Gesundheit, Energie<br>&amp; Lebensfreude</p>
      <p class="cover__author">Dr. med.<br>Birgit Wolkenstein</p>
      <div class="publisher">
        <span class="publisher__dot"></span>
        <span class="publisher__name">Feloria</span>
      </div>
    </section>
  </main>
</body>
</html>
```